Take my logo and make me some cool looking business cards

I've got a logo that we've trademarked so you can't change the logo but you can change it's color combo and find a fun way to incorporate it into a new business card design that is fresh, stylish, and can be applied to some cool medium cost materials (plastic, wood, metal, etc). Basically, we're looking for business cards that stand out in a good way.
Here's the logo we're currently using:
Thanks to everyone that has submitted designs. We've narrowed down to the top 4 designs and tried to eliminate old versions or designs that just didn't match our vision as quickly as we could. We don't plan on keeping this open for the full 9 days; we plan on selecting a design in the next 48 hours; with the goal of having something in the hands of a printer, preferably plastic printer, by Thursday AM Pacific Time.
Business
- must include our existing logo

```html
<!DOCTYPE html>
<html lang="en">
<head>
<meta charset="utf-8">
<title>Halyard Business Card</title>
<link rel="stylesheet" href="https://fonts.googleapis.com/css2?family=Source+Sans+3:wght@400;700&display=swap">
<style>
  :root {
    --backdrop-light: #5c5c5c;
    --backdrop-dark: #3d3d3d;
    --blue-deep: #0c5690;
    --blue-mid: #0f619f;
    --blue-bright: #116bb0;
    --blue-logo: #1a5aa8;
    --silver-edge: #b4b5b8;
    --silver-light: #f4f4f5;
    --ink: #1e1e1e;
    --white: #ffffff;
  }
  * { margin: 0; padding: 0; box-sizing: border-box; }
  html, body { width: 1200px; height: 999px; overflow: hidden; }
  body {
    position: relative;
    background: radial-gradient(ellipse at 50% 40%, var(--backdrop-light), var(--backdrop-dark) 80%);
    font-family: "Source Sans 3", "Myriad Pro", sans-serif;
  }
  .card {
    position: absolute;
    left: 183px;
    width: 792px;
    height: 431px;
    border-radius: 24px;
    overflow: hidden;
    box-shadow: 3px 4px 6px rgba(0,0,0,0.45);
  }
  .band { position: absolute; }

  /* Front */
  .card--front { top: 43px; background: var(--blue-bright); }
  .front-sky {
    left: 0; top: 0; width: 100%; height: 169px;
    background: radial-gradient(ellipse at 45% 40%, #1167a8, var(--blue-deep) 90%);
  }
  .front-name-zone {
    left: 0; top: 169px; width: 100%; height: 58px;
    background: linear-gradient(90deg, var(--blue-deep), var(--blue-mid) 50%, var(--blue-deep));
  }
  .front-tab-left { left: 0; top: 169px; width: 114px; height: 58px; background: var(--blue-bright); }
  .front-tab-right { left: 395px; top: 169px; width: 397px; height: 58px; background: var(--blue-bright); }
  .front-stripe-dark { left: 0; top: 227px; width: 100%; height: 17px; background: var(--blue-deep); }
  .front-stripe-light { left: 0; top: 244px; width: 100%; height: 10px; background: var(--blue-bright); }
  .front-stripe-thin { left: 0; top: 254px; width: 100%; height: 14px; background: var(--blue-deep); }
  .person-name {
    position: absolute; left: 135px; top: 178px;
    font-size: 38px; font-weight: 700; color: var(--white); line-height: 1;
  }
  .person-role {
    position: absolute; left: 406px; top: 196px;
    font-size: 19px; font-weight: 400; color: var(--white); line-height: 1;
  }
  .contact {
    position: absolute; left: 135px; top: 294px;
    font-size: 20px; color: var(--white); line-height: 27px;
  }
  .contact .phone { margin-top: 27px; }

  /* Back */
  .card--back {
    top: 508px;
    background: radial-gradient(ellipse 420px 260px at 48% 42%, var(--white), var(--silver-light) 35%, var(--silver-edge) 100%);
  }
  .back-tab-left {
    left: 0; top: 169px; width: 114px; height: 58px;
    background: linear-gradient(90deg, var(--blue-deep), var(--blue-mid));
  }
  .back-tab-right {
    left: 462px; top: 169px; width: 330px; height: 58px;
    background: linear-gradient(90deg, var(--blue-mid), var(--blue-deep));
  }
  .brand-name {
    position: absolute; left: 137px; top: 166px;
    font-size: 58px; font-weight: 400; letter-spacing: 3px;
    color: var(--blue-logo); line-height: 64px;
  }
  .back-stripe-gray {
    left: 0; width: 100%;
    background: linear-gradient(90deg, #c6c7c9, #f2f2f3 50%, #c6c7c9);
  }
  .back-stripe-a { top: 227px; height: 18px; }
  .back-stripe-b { top: 255px; height: 13px; }
  .back-lower { left: 0; top: 268px; width: 100%; height: 163px; background: var(--white); }
  .website {
    position: absolute; left: 137px; top: 297px;
    font-size: 20px; color: var(--ink); line-height: 1;
  }
</style>
</head>
<body>
  <section class="card card--front" aria-label="Card front">
    <div class="band front-sky"></div>
    <div class="band front-name-zone"></div>
    <div class="band front-tab-left"></div>
    <div class="band front-tab-right"></div>
    <div class="band front-stripe-dark"></div>
    <div class="band front-stripe-light"></div>
    <div class="band front-stripe-thin"></div>
    <h1 class="person-name">Jordan Hale</h1>
    <p class="person-role">CEO</p>
    <address class="contact" style="font-style:normal">
      <div>412 Linden Avenue</div>
      <div>Cedar Cove, CA 94107</div>
      <div class="phone">+15550123456</div>
    </address>
  </section>

  <section class="card card--back" aria-label="Card back">
    <div class="band back-tab-left"></div>
    <div class="band back-tab-right"></div>
    <p class="brand-name">HALYARD</p>
    <div class="band back-stripe-gray back-stripe-a"></div>
    <div class="band back-stripe-gray back-stripe-b"></div>
    <div class="band back-lower"></div>
    <p class="website">www.halyardco.com</p>
  </section>
</body>
</html>
```